Plakate für Lichterabend am Spritzenhaus
Zielgruppe
Als Förderverein der Freiwilligen Feuerwehr Brammhusen betreiben wir jährlich ein 'Lichterabend am Spritzenhaus'. Der Hauptbestandteil der Veranstaltung ist der Verkauf von Weihnachtsbäumen. Bei Bedarf werden diese auch geliefert. Des Weiteren verkaufen wir Grillwurst, Pommes, Waffeln und an unserer Schneebar auch Glühwein und heißen Kakao. Die Kinder haben die Möglichkeit Stockbrot zu backen.
Aufgabenstellung
Wichtig ist ein klarer Bezug zur Feuerwehr und das unser Logo (anbei) sichtbar ist. Die Gestaltung sollte so sein, dass jährlich die 'Tage' mittels neuer Folie ausgetauscht werden können. Es soll also nur '. Dezember' und nicht z.B. '8' aufgedruckt sein.
Wir benötigen einmal die Größe für einen Bauzaun und für einen Banner 4x1m
Anbei das bisherige Design und auch noch ein Flyer-Design, welches wir aktuell für unseren Tag der offenen Tür verwenden.

```html
<!DOCTYPE html>
<html lang="de">
<head>
<meta charset="utf-8">
<title>Lichterabend am Spritzenhaus – Banner</title>
<link rel="stylesheet" href="https://fonts.googleapis.com/css2?family=Fira+Sans+Condensed:ital,wght@1,700;1,800&family=Roboto+Condensed:wght@300;400;700&display=swap">
<style>
  :root {
    --page-bg: #e4e4e4;
    --banner-red: #c1272d;
    --banner-red-dark: #a91f25;
    --banner-dark: #2e2a2b;
    --headline-yellow: #f2c01f;
    --text-white: #ffffff;
    --edge-white: #ffffff;
    --band-red: #c1272d;
    --badge-text: #1e1e1e;
    --tree-green: #3a9a43;
    --tree-green-dark: #2c7a35;
  }
  * { margin: 0; padding: 0; box-sizing: border-box; }
  html, body {
    width: 1200px;
    height: 900px;
    overflow: hidden;
    background: var(--page-bg);
  }
  .banner {
    position: absolute;
    left: 40px;
    top: 310px;
    width: 1120px;
    height: 280px;
    background: var(--banner-red);
    overflow: hidden;
    box-shadow: 0 4px 14px rgba(0,0,0,0.12);
  }
  .band-top {
    position: absolute; left: 0; top: 0; width: 100%; height: 92px;
    background: linear-gradient(180deg, var(--banner-red) 0%, var(--banner-red-dark) 100%);
  }
  .band-dark {
    position: absolute; left: 0; top: 92px; width: 100%; height: 136px;
    background: var(--banner-dark);
  }
  .band-bottom {
    position: absolute; left: 0; top: 228px; width: 100%; height: 52px;
    background: var(--banner-red);
  }
  .festive-illustration {
    position: absolute; left: 20px; top: 96px; width: 216px; height: 184px;
    border-radius: 6px 6px 0 0;
    background: linear-gradient(180deg, var(--tree-green) 0%, var(--tree-green-dark) 100%);
  }
  .headline {
    position: absolute; left: 20px; top: 22px; width: 660px;
    text-align: center;
    font-family: "Fira Sans Condensed", sans-serif;
    font-style: italic; font-weight: 800;
    font-size: 40px; line-height: 46px; letter-spacing: 0.5px;
    color: var(--headline-yellow);
    text-shadow: 0 2px 3px rgba(0,0,0,0.35);
  }
  .event-date {
    position: absolute; left: 200px; top: 110px; width: 450px;
    text-align: center;
    font-family: "Fira Sans Condensed", sans-serif;
    font-style: italic; font-weight: 800;
    font-size: 42px; line-height: 48px;
    color: var(--text-white);
  }
  .day-slot {
    display: inline-block;
    width: 44px;
  }
  .event-venue {
    position: absolute; left: 200px; top: 166px; width: 450px;
    text-align: center;
    font-family: "Fira Sans Condensed", sans-serif;
    font-style: italic; font-weight: 700;
    font-size: 19px; line-height: 24px;
    color: var(--text-white);
  }
  .event-web {
    position: absolute; left: 200px; top: 242px; width: 450px;
    text-align: center;
    font-family: "Fira Sans Condensed", sans-serif;
    font-style: italic; font-weight: 700;
    font-size: 18px; line-height: 22px;
    color: var(--text-white);
  }
  .station-area {
    position: absolute; left: 0; top: 0; width: 1120px; height: 280px;
  }
  .organiser-note {
    position: absolute; left: 770px; top: 78px; width: 215px;
    font-family: "Roboto Condensed", sans-serif;
    font-weight: 300; font-size: 13px; line-height: 17px;
    color: var(--text-white);
  }
  .club-mark {
    position: absolute; left: 985px; top: 32px; width: 110px; height: 110px;
    border-radius: 50%;
    background: var(--text-white);
    display: flex; align-items: center; justify-content: center;
    text-align: center;
    font-family: "Roboto Condensed", sans-serif;
    font-weight: 700; font-size: 13px; line-height: 16px;
    color: var(--badge-text);
    padding: 12px;
  }
</style>
</head>
<body>
  <div class="banner">
    <div class="band-top"></div>
    <div class="band-dark"></div>
    <div class="band-bottom"></div>

    <div class="festive-illustration" role="img" aria-label="Illustration: Weihnachtsbäume, Imbisstisch, Grill mit Flammen und Wimpelkette"></div>

    <h1 class="headline">LICHTERABEND AM SPRITZENHAUS</h1>
    <p class="event-date"><span class="day-slot" aria-label="Tag wird per Folie ergänzt"></span>. Dezember ab 10 Uhr</p>
    <p class="event-venue">Freiwillige Feuerwehr Brammhusen Lindenweg 7</p>
    <p class="event-web">www.ff-brammhusen.de</p>

    <svg class="station-area" viewBox="0 0 1120 280" width="1120" height="280">
      <defs>
        <linearGradient id="stationPhoto" x1="0" y1="0" x2="0" y2="1">
          <stop offset="0" stop-color="#6b6b6b"/>
          <stop offset="0.5" stop-color="#4f4d4d"/>
          <stop offset="0.72" stop-color="#b9453f"/>
          <stop offset="1" stop-color="#d9d4d2"/>
        </linearGradient>
        <clipPath id="stationClip">
          <path d="M760 -4 L718 51 L740 62 L690 115 L704 128 L637 276 L644 284 L1124 284 L1124 -4 Z"/>
        </clipPath>
      </defs>
      <path d="M760 -4 L718 51 L740 62 L690 115 L704 128 L637 276 L644 284 L1124 284 L1124 -4 Z"
            fill="url(#stationPhoto)"
            role="img" aria-label="Foto: Feuerwache mit drei roten Löschfahrzeugen vor den Toren"/>
      <rect class="organiser-band" x="680" y="62" width="440" height="65"
            fill="var(--band-red)" fill-opacity="0.85" clip-path="url(#stationClip)"/>
      <path d="M760 -4 L718 51 L740 62 L690 115 L704 128 L637 276 L644 284"
            fill="none" stroke="var(--edge-white)" stroke-width="10" stroke-linejoin="round"/>
    </svg>

    <p class="organiser-note">Veranstaltet vom Förderverein der Freiwilligen Feuerwehr Brammhusen e.V.</p>
    <div class="club-mark">Förderverein FF Brammhusen</div>
  </div>
</body>
</html>
```